RFID Blocker - Business Card Design

Design a business card that will be printed onto a plastic RFID blocker wallet card, this card has a space on each side of teh card that will not be printed. One side of the card is to have the contact information, and the other to have a graphic which will symbolize blocking or shielding technology. I like the phrase "Fold Haven". Many people i give this card to may not realize it is a RFID blocker, and i would liek to have small icons on each side representing what it is, see attachment. I will include a few pics found on internet i was using as ideas, and also the RFID card template which shows the area that will not be printed (within the red squares). I like the shield aspect, i was originally thinking of the tarnwick shield with my logo coming out of it like the tarnwick except the black is to dark of a color. the smiley face i use within some of my software. company name is: "vornalux software inc." - I prefer to use small print and no capitals in my company name. company from Canada - my original business card is included in files

Target Market(s)

companies wanting to hire indigenous workers, and indigenous workers looking for employment

Contact Information for Business Card

should include logo with name, title, phone, email and website. our company specializes in first nations indigenous employment software

Font styles to use
Serif
Sans Serif

Requirements
Must have
• Logo
• Name
• Title
• Phone
• email
• website

```html
<!DOCTYPE html>
<html lang="en">
<head>
<meta charset="utf-8">
<title>vornalux software inc. – business card</title>
<link rel="stylesheet" href="https://fonts.googleapis.com/css2?family=Open+Sans:wght@400;600;700&display=swap">
<style>
  :root {
    --backdrop: #ececec;
    --card-white: #fbfbfb;
    --brand-blue: #1a6fc9;
    --ink-grey: #5b6068;
    --ink-dark: #3a3f46;
    --night-deep: #06141c;
    --night-mid: #0b3344;
    --cyan-glow: #2fb8d6;
    --light-text: #ffffff;
  }
  * { margin: 0; padding: 0; box-sizing: border-box; }
  html, body {
    width: 1200px; height: 800px; overflow: hidden;
    background: var(--backdrop);
    font-family: "Open Sans", Arial, sans-serif;
  }
  .sheet {
    position: relative; width: 1200px; height: 800px;
    display: flex; align-items: center; justify-content: center; gap: 50px;
  }
  .card {
    position: relative; width: 525px; height: 300px; overflow: hidden;
    box-shadow: 0 6px 18px rgba(0,0,0,0.12);
  }

  /* Graphic side */
  .card--graphic { background: var(--night-deep); }
  .graphic-art {
    position: absolute; inset: 0;
    background:
      radial-gradient(circle at 26% 58%, rgba(47,184,214,0.75) 0, rgba(47,184,214,0.25) 18%, transparent 34%),
      linear-gradient(135deg, var(--night-deep) 0%, var(--night-mid) 55%, var(--night-deep) 100%);
  }
  .graphic-brand {
    position: absolute; right: 48px; top: 92px;
    color: var(--light-text);
  }
  .graphic-brand .brand-name {
    font-size: 52px; font-weight: 600; letter-spacing: -0.5px; line-height: 1;
  }
  .graphic-brand .brand-web {
    font-size: 13px; font-weight: 400; margin-top: 8px; padding-left: 46px;
  }

  /* Contact side */
  .card--contact { background: var(--card-white); }
  .edge-tab {
    position: absolute; right: 0; top: 0; width: 12px; height: 46px;
    background: var(--brand-blue); border-bottom-left-radius: 4px;
  }
  .contact-brand {
    position: absolute; left: 38px; top: 52px;
    font-size: 54px; font-weight: 600; color: var(--ink-grey);
    letter-spacing: -0.5px; line-height: 1;
  }
  .person {
    position: absolute; right: 40px; top: 48px; text-align: right;
  }
  .person .person-name {
    font-size: 24px; font-weight: 700; color: var(--brand-blue); line-height: 1.1;
  }
  .person .person-title {
    font-size: 14px; font-weight: 400; color: var(--ink-grey); margin-top: 2px;
  }
  .contact-list {
    position: absolute; left: 38px; top: 168px; list-style: none;
    font-size: 13px; color: var(--ink-dark); line-height: 22px;
  }
  .contact-list li { display: flex; align-items: center; gap: 8px; }
  .contact-list svg { width: 12px; height: 12px; flex: none; }
  .icon-fill { fill: var(--brand-blue); }
  .icon-line { fill: none; stroke: var(--brand-blue); stroke-width: 2.4; stroke-linejoin: round; }
  .tagline-band {
    position: absolute; left: 0; right: 0; bottom: 0; height: 40px;
    background: var(--brand-blue); color: var(--light-text);
    display: flex; align-items: center; justify-content: center;
    font-size: 18px; font-weight: 400; letter-spacing: 1px;
  }
</style>
</head>
<body>
<main class="sheet">
  <section class="card card--graphic">
    <div class="graphic-art" role="img" aria-label="Glowing blue shield with keyhole over a dark field of digital code"></div>
    <div class="graphic-brand">
      <div class="brand-name">vornalux</div>
      <div class="brand-web">www.vornalux.ca</div>
    </div>
  </section>

  <section class="card card--contact">
    <div class="edge-tab"></div>
    <div class="contact-brand">vornalux</div>
    <div class="person">
      <div class="person-name">Dale Rennick</div>
      <div class="person-title">President</div>
    </div>
    <ul class="contact-list">
      <li>
        <svg viewBox="0 0 24 24" aria-hidden="true"><path class="icon-fill" d="M6.6 10.8a15.1 15.1 0 0 0 6.6 6.6l2.2-2.2a1 1 0 0 1 1-.25 11.4 11.4 0 0 0 3.6.57 1 1 0 0 1 1 1V20a1 1 0 0 1-1 1A17 17 0 0 1 3 4a1 1 0 0 1 1-1h3.5a1 1 0 0 1 1 1c0 1.25.2 2.45.57 3.6a1 1 0 0 1-.25 1z"/></svg>
        (250) 555-0147
      </li>
      <li>
        <svg viewBox="0 0 24 24" aria-hidden="true"><path class="icon-line" d="M3 6h18v12H3z M3 6l9 7 9-7"/></svg>
        drennick@vornalux.ca
      </li>
      <li>
        <svg viewBox="0 0 24 24" aria-hidden="true"><circle class="icon-line" cx="12" cy="12" r="9"/><path class="icon-line" d="M3 12h18 M12 3c3 3 3 15 0 18 M12 3c-3 3-3 15 0 18"/></svg>
        www.vornalux.ca
      </li>
    </ul>
    <div class="tagline-band">Hiring Tools Built For First Nations</div>
  </section>
</main>
</body>
</html>
```